This is a label for a new sake made in Japan imported into Aust

This will be a bottle label for a new sake imported into Australia. The hero of the label is the Trelu. We have joined the "O" meaning great in Japanese and used sake with "Z" to have Trelu with the play on words using Oz as in our slang for Aussie. A modern label with a Japanese take is key. This is a premium sake made in Japan for the Australian market.
The "Lark Hollow" up the top is the name of the company, we have yet to design a logo for the company.

Target Market(s)

Alcohol

Logo Text

Trelu

Font styles to use
Serif

Requirements
Must have
• easy to read, with a hint of Japanese origin
Should not have
• too busy

```html
<!DOCTYPE html>
<html lang="en">
<head>
<meta charset="utf-8">
<title>Trelu – Premium Sake Label</title>
<link href="https://fonts.googleapis.com/css2?family=Josefin+Sans:wght@300;600;700&family=Cormorant+Garamond:wght@500&display=swap" rel="stylesheet">
<style>
  :root {
    --page: #ffffff;
    --label-black: #1c1b1c;
    --sake-red: #c4232e;
    --paper-white: #f4f4f4;
    --strip-grey: #e6e6e6;
    --strip-text: #a9a9a9;
    --spec-text: #444444;
    --spec-rule: #999999;
  }
  * { box-sizing: border-box; margin: 0; padding: 0; }
  html, body {
    width: 1106px;
    height: 1200px;
    overflow: hidden;
    background: var(--page);
  }
  .label {
    position: absolute;
    left: 123px;
    top: 150px;
    width: 860px;
  }
  .label-panel {
    position: relative;
    width: 860px;
    height: 850px;
    background: var(--label-black);
  }
  .company-name {
    position: absolute;
    left: 200px;
    top: 78px;
    font-family: "Josefin Sans", sans-serif;
    font-weight: 300;
    font-size: 60px;
    letter-spacing: 3px;
    color: var(--paper-white);
    text-transform: uppercase;
    white-space: nowrap;
  }
  .spec-box {
    position: absolute;
    left: 729px;
    top: 33px;
    width: 113px;
    height: 346px;
    background: var(--sake-red);
    padding: 12px;
  }
  .spec-inner {
    width: 100%;
    height: 100%;
    background: var(--paper-white);
    display: flex;
    flex-direction: column;
    font-family: "Cormorant Garamond", serif;
    font-weight: 500;
    font-size: 24px;
    color: var(--spec-text);
    text-align: center;
    white-space: nowrap;
  }
  .spec-item {
    flex: 1;
    display: flex;
    flex-direction: column;
    justify-content: center;
    line-height: 1.4;
  }
  .spec-item + .spec-item { border-top: 2px solid var(--spec-rule); margin: 0 8px; }
  .brand-mark {
    position: absolute;
    left: 70px;
    top: 500px;
    display: flex;
    align-items: center;
    gap: 36px;
  }
  .brand-square {
    width: 64px;
    height: 64px;
    background: var(--sake-red);
  }
  .brand-name {
    font-family: "Josefin Sans", sans-serif;
    font-weight: 700;
    font-size: 150px;
    line-height: 1;
    color: var(--paper-white);
    letter-spacing: 4px;
    padding-top: 28px;
    white-space: nowrap;
  }
  .tagline-strip {
    width: 860px;
    height: 64px;
    margin-top: 18px;
    background: var(--strip-grey);
    display: flex;
    align-items: center;
    justify-content: center;
    font-family: "Josefin Sans", sans-serif;
    font-weight: 600;
    font-size: 32px;
    letter-spacing: 5px;
    color: var(--strip-text);
    text-transform: uppercase;
  }
</style>
</head>
<body>
  <div class="label">
    <div class="label-panel">
      <div class="company-name">Lark Hollow</div>
      <div class="spec-box">
        <div class="spec-inner">
          <div class="spec-item"><span>ALC</span><span>16%</span></div>
          <div class="spec-item"><span>VOL</span><span>720 ml</span></div>
        </div>
      </div>
      <div class="brand-mark">
        <div class="brand-square" aria-hidden="true"></div>
        <div class="brand-name">TRELU</div>
      </div>
    </div>
    <div class="tagline-strip">Premium Japanesse Sake</div>
  </div>
</body>
</html>
```